A resume/portfolio website for myself

I'm an independent software contractor, architect, tech trainer. I need a web site to present myself. Many ready to use portfolio designs are too artistic and focused on presenting design skills of the person. I like a nice website but the content should be a little less graphic than if you would present a graphic designer. Content could be presentation of me, core skill qualities and services and resume. Potentially a page with my tech courses in the longer run

```html
<!DOCTYPE html>
<html lang="en">
<head>
<meta charset="utf-8">
<title>Daniel Marsh – Resume</title>
<link rel="stylesheet" href="https://fonts.googleapis.com/css2?family=Roboto:wght@400;500;700;900&display=swap">
<style>
:root{
  --blue:#2fa3da;
  --ink:#111111;
  --text:#444444;
  --grey-band:#ebebeb;
  --light-band:#dcf0f9;
  --track:#ffffff;
  --footer:#050505;
  --white:#ffffff;
}
*{margin:0;padding:0;box-sizing:border-box}
html,body{width:1200px;height:3886px;overflow:hidden}
body{position:relative;font-family:'Roboto',sans-serif;color:var(--ink);background:var(--white)}

/* hero */
.hero{position:absolute;left:0;top:0;width:1200px;height:703px;
  background:linear-gradient(90deg,#2d3a1c 0%,#4a6a2a 22%,#6f8d80 48%,#4f6a34 72%,#2a3520 100%);}
.hero::after{content:"";position:absolute;inset:0;background:linear-gradient(180deg,rgba(0,0,0,0) 55%,rgba(20,25,25,.55) 100%)}
.nav{position:absolute;top:44px;left:0;width:1200px;height:30px;z-index:2}
.nav a{position:absolute;color:var(--white);font-size:15px;font-weight:500;text-decoration:none}
.nav a.active::after{content:"";position:absolute;left:0;right:0;bottom:-8px;height:2px;background:var(--white)}
.hero-panel{position:absolute;left:540px;top:219px;width:660px;height:324px;background:var(--blue);z-index:2}
.portrait{position:absolute;left:365px;top:217px;width:326px;height:326px;border-radius:50%;
  border:4px solid var(--white);background:radial-gradient(circle at 45% 40%,#b79a83,#6f6150 55%,#4d4a3b);z-index:3}
.hello{position:absolute;left:739px;top:249px;width:118px;height:41px;background:var(--white);color:var(--blue);
  border-radius:14px 0 14px 0;font-size:17px;font-weight:500;line-height:41px;text-align:center;z-index:4}
.hero-name{position:absolute;left:739px;top:298px;font-size:46px;font-weight:900;color:var(--white);z-index:4}
.hero-role{position:absolute;left:739px;top:347px;font-size:21px;font-weight:500;color:var(--white);z-index:4}
.hero-contact{position:absolute;left:739px;z-index:4;color:var(--white);font-size:15px;font-weight:500;display:flex;align-items:center;gap:18px}
.social{position:absolute;display:flex;gap:10px;z-index:4}
.social span{display:block;border-radius:50%}

/* headings */
.eyebrow{position:absolute;color:var(--blue);font-size:17px;font-weight:400;letter-spacing:.3px}
.h2{position:absolute;font-size:39px;font-weight:900;color:var(--ink);letter-spacing:.3px}
.blue{color:var(--blue)}

/* about */
.about-frame{position:absolute;left:183px;top:893px;width:252px;height:269px;border:5px solid var(--blue);border-left:none;border-top:none;border-radius:0 0 34px 0}
.about-photo{position:absolute;left:163px;top:874px;width:253px;height:270px;background:linear-gradient(135deg,#2f4a22,#5c6e3c 45%,#3a3a30);border-bottom:4px solid var(--white)}
.about-title{position:absolute;left:575px;top:853px;font-size:21px;font-weight:500}
.about-text{position:absolute;left:575px;font-size:15px;line-height:24.5px;color:var(--text);white-space:nowrap}
.btn{position:absolute;background:var(--blue);color:var(--white);font-weight:500;text-align:center;border-radius:18px 0 18px 0}

/* services */
.service{position:absolute;top:1350px;width:310px}
.service svg{display:block;height:40px}
.service h3{margin-top:18px;font-size:20px;font-weight:500}
.service p{margin-top:15px;font-size:15px;line-height:24.5px;color:var(--text)}

/* skills */
.skills{position:absolute;left:0;top:1628px;width:1200px;height:394px;background:var(--grey-band)}
.skill-h{position:absolute;top:32px;font-size:34px;font-weight:900}
.bar{position:absolute;width:418px;height:5px;background:var(--track);border-radius:3px}
.bar i{position:absolute;left:0;top:0;height:5px;background:var(--blue);border-radius:3px}
.bar i::after{content:"";position:absolute;right:-8px;top:-5px;width:15px;height:15px;border-radius:50%;background:var(--blue)}
.skill-label{position:absolute;font-size:17px;color:var(--ink)}

/* education */
.edu-crest{position:absolute;left:160px;width:80px;height:80px;border-radius:50%;border:3px solid #3c4a6a}
.edu-title{position:absolute;left:262px;font-size:28px;font-weight:500;line-height:36px}
.edu-year{position:absolute;left:262px;font-size:17px;font-weight:500;color:var(--blue)}
.edu-text{position:absolute;left:631px;font-size:12.5px;line-height:21px;color:var(--text);font-weight:500;white-space:nowrap}
.vline{position:absolute;width:1px;background:#cfcfcf}
.hline{position:absolute;height:1px;background:#cfcfcf}

/* experience */
.work{position:absolute;left:0;top:2643px;width:1200px;height:614px;background:var(--light-band)}
.job{position:absolute;width:420px}
.job h4{font-size:28px;font-weight:500;line-height:34px}
.job .yr{margin-top:14px;font-size:17px;font-weight:500;color:var(--blue)}
.job .resp{margin-top:14px;font-size:13px;font-weight:700}
.job ul{list-style:none;margin-top:10px}
.job li{position:relative;padding-left:52px;font-size:15px;color:var(--text);line-height:38px}
.job li::before{content:"";position:absolute;left:21px;top:14px;width:11px;height:11px;border-radius:50%;background:var(--blue)}

/* contact */
.contact-line{position:absolute;left:142px;display:flex;align-items:center;gap:14px;font-size:15px;color:var(--text)}
.field{position:absolute;border:2px solid #d6d6d6;border-radius:14px 0 14px 0;font-size:12px;color:#555;padding:12px 14px}

/* footer */
.footer{position:absolute;left:0;top:3729px;width:1200px;height:157px;background:var(--footer)}
.footer p{position:absolute;top:96px;width:1200px;text-align:center;color:var(--white);font-size:15px;font-weight:500}
</style>
</head>
<body>

<header class="hero" role="img" aria-label="Photo of a mossy canyon with a waterfall and a stream"></header>
<nav class="nav">
  <a class="active" href="#" style="left:334px">Home</a>
  <a href="#" style="left:415px">About</a>
  <a href="#" style="left:497px">Skills</a>
  <a href="#" style="left:575px">Education</a>
  <a href="#" style="left:685px">Experiences</a>
  <a href="#" style="left:810px">Contact</a>
</nav>
<div class="hero-panel"></div>
<div class="portrait" role="img" aria-label="Portrait photo of Daniel Marsh"></div>
<div class="hello">Hello I'm</div>
<h1 class="hero-name">Daniel Marsh</h1>
<div class="hero-role">Graphic Designer</div>
<div class="hero-contact" style="top:390px">
  <svg width="15" height="12" viewBox="0 0 15 12"><rect width="15" height="12" rx="1.5" fill="#fff"/><path d="M1 1.5 7.5 7 14 1.5" stroke="#2fa3da" stroke-width="1.6" fill="none"/></svg>hello@danielmarsh.dev</div>
<div class="hero-contact" style="top:422px">
  <svg width="15" height="15" viewBox="0 0 24 24"><path fill="#fff" d="M6.6 10.8a15 15 0 0 0 6.6 6.6l2.2-2.2c.3-.3.7-.4 1-.2 1.1.4 2.3.6 3.6.6.6 0 1 .4 1 1V20c0 .6-.4 1-1 1A17 17 0 0 1 3 4c0-.6.4-1 1-1h3.5c.6 0 1 .4 1 1 0 1.3.2 2.5.6 3.6.1.3 0 .7-.2 1z"/></svg>555 0142 318</div>
<div class="hero-contact" style="top:453px">
  <svg width="13" height="17" viewBox="0 0 24 32"><path fill="#fff" d="M12 0A12 12 0 0 0 0 12c0 9 12 20 12 20s12-11 12-20A12 12 0 0 0 12 0zm0 17a5 5 0 1 1 0-10 5 5 0 0 1 0 10z"/></svg>Lindenweg 12, 4031 Harbourton, Westland</div>
<div class="social" style="left:739px;top:498px">
  <span style="width:13px;height:13px;background:#fff"></span><span style="width:13px;height:13px;background:#fff"></span><span style="width:13px;height:13px;background:#fff"></span><span style="width:13px;height:13px;background:#fff"></span>
</div>

<!-- about -->
<div class="eyebrow" style="left:106px;top:787px">BIOGRAPHY</div>
<h2 class="h2" style="left:106px;top:815px">ABOUT ME</h2>
<div class="about-frame"></div>
<div class="about-photo" role="img" aria-label="Photo of Daniel Marsh seated in front of green foliage"></div>
<div class="about-title">I'm Daniel Marsh and <span class="blue">Graphic Designer</span></div>
<p class="about-text" style="top:893px">Hi! My name is <span class="blue">Daniel Marsh</span>. I am a <span class="blue">Graphic Designer</span>, and I'm very<br>passionate and dedicated to my work. With 20 years experience as<br>a professional Web developer, I have acquired the skills and knowledge<br>necessary to make your project a success.</p>
<p class="about-text" style="top:1016px">Praesent sed aliquam arcu, non accumsan neque. In odio ante, vulputate<br>ac magna vel, pharetra lobortis quam. Duis enim tortor, egestas et felis id,<br>lobortis malesuada magna. Nunc sit amet sagittis nisi, eu semper nisl.<br>Cras ut dictum nisl. Donec tincidunt eget orci.</p>
<div class="btn" style="left:578px;top:1138px;width:152px;height:41px;line-height:41px;font-size:15px">Download CV</div>

<!-- services -->
<div class="eyebrow" style="left:103px;top:1264px">SERVICES</div>
<h2 class="h2" style="left:103px;top:1290px">WHAT I DO</h2>
<div class="service" style="left:130px">
  <svg width="24" height="36" viewBox="0 0 24 36"><path fill="#2fa3da" d="M12 0 22 14v10H2V14z"/><rect x="2" y="27" width="20" height="6" rx="1" fill="#2fa3da"/><circle cx="12" cy="15" r="3" fill="#fff"/><rect x="11" y="4" width="2" height="9" fill="#fff"/></svg>
  <h3>UI Design</h3>
  <p>Lorem ipsum dolor sit amet, consectetuer adipiscing elit, sed diam nonummy nibh euismod tincidunt ut laoreet dolore magna aliquam erat volutpat.</p>
</div>
<div class="service" style="left:463px">
  <svg width="64" height="36" viewBox="0 0 64 36"><path d="M14 5 3 18l11 13M50 5l11 13-11 13" stroke="#2fa3da" stroke-width="4" fill="none" stroke-linecap="round" stroke-linejoin="round"/><circle cx="32" cy="18" r="9" fill="none" stroke="#2fa3da" stroke-width="5" stroke-dasharray="4 3"/><circle cx="32" cy="18" r="3" fill="#2fa3da"/></svg>
  <h3>Web Development</h3>
  <p>Lorem ipsum dolor sit amet, consectetuer adipiscing elit, sed diam nonummy nibh euismod tincidunt ut laoreet dolore magna aliquam erat volutpat.</p>
</div>
<div class="service" style="left:797px">
  <svg width="56" height="36" viewBox="0 0 56 36"><rect x="2" y="8" width="52" height="26" rx="6" fill="#2fa3da"/></svg>
  <h3>App Development</h3>
  <p>Lorem ipsum dolor sit amet, consectetuer adipiscing elit, sed diam nonummy nibh euismod tincidunt ut laoreet dolore magna aliquam erat volutpat.</p>
</div>

<!-- skills -->
<section class="skills">
  <h2 class="skill-h" style="left:88px">TECHNICAL SKILLS</h2>
  <h2 class="skill-h" style="left:693px">PROFESSIONAL SKILLS</h2>

  <div class="bar" style="left:88px;top:102px"><i style="width:74%"></i></div>
  <div class="skill-label" style="left:86px;top:119px">Pagecraft</div><div class="skill-label" style="left:385px;top:119px">80%</div>
  <div class="bar" style="left:88px;top:157px"><i style="width:60%"></i></div>
  <div class="skill-label" style="left:86px;top:174px">Nodeleaf</div><div class="skill-label" style="left:327px;top:174px">61%</div>
  <div class="bar" style="left:88px;top:213px"><i style="width:94%"></i></div>
  <div class="skill-label" style="left:86px;top:229px">PHP &amp; SQL</div><div class="skill-label" style="left:470px;top:229px">99%</div>
  <div class="bar" style="left:88px;top:269px"><i style="width:91%"></i></div>
  <div class="skill-label" style="left:86px;top:286px">Pixelforge</div><div class="skill-label" style="left:458px;top:286px">97%</div>
  <div class="bar" style="left:88px;top:325px"><i style="width:84%"></i></div>
  <div class="skill-label" style="left:86px;top:341px">HTML &amp; CSS</div><div class="skill-label" style="left:429px;top:341px">89%</div>

  <div class="bar" style="left:694px;top:102px"><i style="width:88%"></i></div>
  <div class="skill-label" style="left:694px;top:119px">Communication</div><div class="skill-label" style="left:1050px;top:119px">95%</div>
  <div class="bar" style="left:694px;top:157px"><i style="width:73%"></i></div>
  <div class="skill-label" style="left:694px;top:174px">Team Work</div><div class="skill-label" style="left:988px;top:174px">85%</div>
  <div class="bar" style="left:694px;top:213px"><i style="width:63%"></i></div>
  <div class="skill-label" style="left:694px;top:229px">Project Management</div><div class="skill-label" style="left:944px;top:229px">79%</div>
  <div class="bar" style="left:694px;top:269px"><i style="width:52%"></i></div>
  <div class="skill-label" style="left:694px;top:286px">Creativity</div><div class="skill-label" style="left:900px;top:286px">64%</div>
</section>

<!-- education -->
<h2 class="h2" style="left:0;width:1200px;text-align:center;top:2102px">EDUCATION</h2>

<div class="edu-crest" style="top:2177px"></div>
<div class="edu-title" style="top:2164px">Art &amp; Multimedia From<br><span class="blue">Northbridge University</span></div>
<div class="edu-year" style="top:2250px">2011-2013</div>
<div class="vline" style="left:599px;top:2182px;height:70px"></div>
<p class="edu-text" style="top:2187px">It is a long established fact that a reader will be distracted by the<br>readable content of a page when looking at its layout.<br>The point of using Lorem Ipsum</p>
<div class="hline" style="left:599px;top:2291px;width:439px"></div>

<div class="edu-crest" style="top:2321px"></div>
<div class="edu-title" style="top:2308px">Art &amp; Multimedia From<br><span class="blue">Northbridge University</span></div>
<div class="edu-year" style="top:2394px">2008-2011</div>
<div class="vline" style="left:599px;top:2326px;height:70px"></div>
<p class="edu-text" style="top:2331px">It is a long established fact that a reader will be distracted by the<br>readable content of a page when looking at its layout.<br>The point of using Lorem Ipsum</p>
<div class="hline" style="left:599px;top:2435px;width:439px"></div>

<div class="edu-crest" style="top:2465px"></div>
<div class="edu-title" style="top:2452px">Art &amp; Multimedia From<br><span class="blue">Northbridge University</span></div>
<div class="edu-year" style="top:2538px">2005-2008</div>
<div class="vline" style="left:599px;top:2470px;height:70px"></div>
<p class="edu-text" style="top:2475px">It is a long established fact that a reader will be distracted by the<br>readable content of a page when looking at its layout.<br>The point of using Lorem Ipsum</p>

<!-- experience -->
<section class="work">
  <div class="eyebrow" style="left:0;width:1200px;text-align:center;top:56px">TIMELINE</div>
  <h2 class="h2" style="left:0;width:1200px;text-align:center;top:82px">WORK EXPERIENCE</h2>
  <div class="vline" style="left:600px;top:182px;height:133px"></div>
  <div class="vline" style="left:600px;top:408px;height:133px"></div>

  <div class="job" style="left:180px;top:148px"><h4>UI/UX Designer <span class="blue">Quarrystone</span></h4><div class="yr">2013-2015</div><div class="resp">Responsibility :</div><ul><li>Validate CSS</li><li>Project Management</li></ul></div>
  <div class="job" style="left:663px;top:148px"><h4>UI/UX Designer <span class="blue">Quarrystone</span></h4><div class="yr">2015-2017</div><div class="resp">Responsibility :</div><ul><li>Validate CSS</li><li>Project Management</li></ul></div>
  <div class="job" style="left:180px;top:375px"><h4>UI/UX Designer <span class="blue">Quarrystone</span></h4><div class="yr">2017-2018</div><div class="resp">Responsibility :</div><ul><li>Validate CSS</li><li>Project Management</li></ul></div>
  <div class="job" style="left:663px;top:375px"><h4>UI/UX Designer <span class="blue">Quarrystone</span></h4><div class="yr">2018-2020</div><div class="resp">Responsibility :</div><ul><li>Validate CSS</li><li>Project Management</li></ul></div>
</section>

<!-- contact -->
<div class="eyebrow" style="left:86px;top:3342px">CONTACT</div>
<h2 class="h2" style="left:86px;top:3369px">GET IN TOUCH</h2>
<div class="contact-line" style="top:3434px"><svg width="15" height="12" viewBox="0 0 15 12"><rect width="15" height="12" rx="1.5" fill="#2fa3da"/><path d="M1 1.5 7.5 7 14 1.5" stroke="#fff" stroke-width="1.6" fill="none"/></svg>hello@danielmarsh.dev</div>
<div class="contact-line" style="top:3465px"><svg width="15" height="15" viewBox="0 0 24 24"><path fill="#2fa3da" d="M6.6 10.8a15 15 0 0 0 6.6 6.6l2.2-2.2c.3-.3.7-.4 1-.2 1.1.4 2.3.6 3.6.6.6 0 1 .4 1 1V20c0 .6-.4 1-1 1A17 17 0 0 1 3 4c0-.6.4-1 1-1h3.5c.6 0 1 .4 1 1 0 1.3.2 2.5.6 3.6.1.3 0 .7-.2 1z"/></svg>555 0142 318</div>
<div class="contact-line" style="top:3497px"><svg width="13" height="17" viewBox="0 0 24 32"><path fill="#2fa3da" d="M12 0A12 12 0 0 0 0 12c0 9 12 20 12 20s12-11 12-20A12 12 0 0 0 12 0zm0 17a5 5 0 1 1 0-10 5 5 0 0 1 0 10z"/></svg>Lindenweg 12, 4031 Harbourton, Westland</div>
<div class="social" style="left:134px;top:3542px;gap:16px">
  <span style="width:18px;height:18px;background:var(--blue)"></span><span style="width:18px;height:18px;background:var(--blue)"></span><span style="width:18px;height:18px;background:var(--blue)"></span><span style="width:18px;height:18px;background:var(--blue)"></span>
</div>

<div class="field" style="left:567px;top:3347px;width:261px;height:41px">First Name</div>
<div class="field" style="left:850px;top:3347px;width:262px;height:41px">Last Name</div>
<div class="field" style="left:567px;top:3404px;width:545px;height:41px">Your Email</div>
<div class="field" style="left:567px;top:3462px;width:545px;height:114px">Message</div>
<div class="btn" style="left:850px;top:3597px;width:262px;height:43px;line-height:43px;font-size:15px">SEND MESSAGE</div>

<footer class="footer">
  <div class="social" style="left:521px;top:45px;gap:22px">
    <span style="width:24px;height:24px;background:var(--blue)"></span><span style="width:24px;height:24px;background:var(--blue)"></span><span style="width:24px;height:24px;background:var(--blue)"></span><span style="width:24px;height:24px;background:var(--blue)"></span>
  </div>
  <p>All right reserved danielmarsh @ 2020</p>
</footer>

</body>
</html>
```